Copper lark buildworks

Copper lark buildworks is a small construction company.
Who is a licenced builder, Carpenter, joiner,
working on heritage ,new build, speacial projects and sometimes furniture

Industry/Entity Type

Construction

```html
<!DOCTYPE html>
<html lang="en">
<head>
<meta charset="utf-8">
<title>Copper lark buildworks – business card</title>
<link href="https://fonts.googleapis.com/css2?family=Open+Sans:wght@400;600&family=Noto+Serif:wght@400&family=Inconsolata:wght@400&display=swap" rel="stylesheet">
<style>
  :root {
    --backdrop: #262626;
    --card-light: #ebebeb;
    --card-dark: #2e2e2e;
    --rule: #d2d2d2;
    --ink: #3c3c3c;
    --ink-soft: #555555;
    --accent-green: #2fae3c;
    --number-green: #2bb673;
    --icon-blue: #5ab8e8;
    --icon-glow: rgba(90, 184, 232, 0.55);
  }
  * { margin: 0; padding: 0; box-sizing: border-box; }
  html, body {
    width: 1200px;
    height: 800px;
    overflow: hidden;
    background: var(--backdrop);
  }
  .stage {
    position: relative;
    width: 1200px;
    height: 800px;
    display: flex;
    align-items: center;
    justify-content: center;
    gap: 60px;
  }
  .card {
    position: relative;
    width: 490px;
    height: 280px;
    border-radius: 10px;
    box-shadow: 0 10px 30px rgba(0, 0, 0, 0.45);
  }
  /* Front */
  .card--front {
    background: var(--card-light);
    text-align: center;
  }
  .card__rule {
    position: absolute;
    left: 90px;
    right: 90px;
    height: 1px;
    background: var(--rule);
  }
  .card__rule--top { top: 48px; }
  .card__rule--bottom { bottom: 40px; }
  .company {
    position: absolute;
    top: 62px;
    left: 0;
    right: 0;
  }
  .company__name {
    font-family: "Open Sans", sans-serif;
    font-weight: 400;
    font-size: 22px;
    color: var(--ink);
    letter-spacing: 0.2px;
  }
  .company__tagline {
    font-family: "Open Sans", sans-serif;
    font-size: 11px;
    color: var(--accent-green);
    margin-top: 2px;
  }
  .person {
    position: absolute;
    top: 170px;
    left: 0;
    right: 0;
  }
  .person__name {
    font-family: "Open Sans", sans-serif;
    font-size: 20px;
    color: var(--ink);
  }
  .person__role {
    font-family: "Noto Serif", serif;
    font-size: 12px;
    color: var(--ink-soft);
    margin-top: 1px;
  }
  /* Back */
  .card--back {
    background: var(--card-dark);
  }
  .contact-icons {
    position: absolute;
    left: 150px;
    top: 42px;
    display: flex;
    flex-direction: column;
    gap: 22px;
  }
  .contact-icon {
    width: 36px;
    height: 36px;
    border-radius: 50%;
    background: var(--icon-blue);
    box-shadow: 0 0 18px 6px var(--icon-glow);
    display: flex;
    align-items: center;
    justify-content: center;
  }
  .contact-number {
    position: absolute;
    left: 240px;
    top: 168px;
    font-family: "Inconsolata", monospace;
    font-size: 20px;
    letter-spacing: 1.5px;
    color: var(--number-green);
  }
</style>
</head>
<body>
<main class="stage">
  <section class="card card--front">
    <div class="card__rule card__rule--top"></div>
    <div class="company">
      <h1 class="company__name">Copper lark buildworks</h1>
      <p class="company__tagline">construction company</p>
    </div>
    <div class="person">
      <h2 class="person__name">Tobias Marlow</h2>
      <p class="person__role">company orner</p>
    </div>
    <div class="card__rule card__rule--bottom"></div>
  </section>

  <section class="card card--back">
    <div class="contact-icons">
      <span class="contact-icon" aria-label="location">
        <svg width="16" height="18" viewBox="0 0 16 18"><path d="M8 1a5.5 5.5 0 0 0-5.5 5.5C2.5 11 8 17 8 17s5.5-6 5.5-10.5A5.5 5.5 0 0 0 8 1z" fill="#ffffff"/><circle cx="8" cy="6.5" r="2" fill="#5ab8e8"/></svg>
      </span>
      <span class="contact-icon" aria-label="phone">
        <svg width="16" height="16" viewBox="0 0 16 16"><path d="M4 1.5l2.2 3-1.3 1.6c.8 1.8 2.2 3.2 4 4l1.6-1.3 3 2.2-1.2 2.5C7 13.3 2.7 9 1.5 3.2z" fill="#ffffff"/></svg>
      </span>
      <span class="contact-icon" aria-label="email">
        <svg width="18" height="14" viewBox="0 0 18 14"><rect x="1" y="1.5" width="16" height="11" rx="1" fill="#ffffff"/><path d="M1.5 2l7.5 6 7.5-6" fill="none" stroke="#5ab8e8" stroke-width="1.2"/></svg>
      </span>
    </div>
    <p class="contact-number">0491570156</p>
  </section>
</main>
</body>
</html>
```